Architecture office 10 pages brochure for investors

We need a multi-page brochure (10pg) for our small architectural office.
After the long real estate crisis in Greece we're intend to reborn our architectural planning services, to relocate our targets and to communicate the philosophy in the new era of commercial buildings:
Modern architectural language, Highly energy efficient buildings with green and passive oriented design and functional details. Multifamily housing, Office buildings, Hotels, Refurbishment and Interiors from a group of new architects collaborators and an experienced leader.
We need fresh, clever styling with minimal expression and reach meanings. Written in two languages (ENG-GR) the fonts must be compatible. The solution of an digital and non-printed brochure, for on-line sharing, its a possibility and maybe unlock animated and / or AR solutions. The green color -as attached- will be appreciated.

Please provide your professional opinion about the set up of the pages.
An idea given: minimal frontpage, 2-3nd pages "about us" and "contents with photo and some minor text, and every next page refers one selected project with photo and some text for two languages (4-7 pages projects), pages 8-9 listed works-projects, collaborators, clients.
Updates

low design entries -one entry as 4 projects- , low quality, not satisfying the wills

Target Market(s)

investors in commercial buildings, private clients, energy efficiency

Industry/Entity Type

Architecture

Font styles to use
Sans Serif
Other font styles liked:
• greek compatible

Requirements
Must have
• clear - minimal design, photos, illustrations, text, contents.
• some of the projects can find them in attached link,
Nice to have
• dynamic lines, hand drawing sketches
• maybe the building design process: thoughts, sketch, hand design, cad, collaboration with other engineers, 3d renderings, animations ....
Should not have
• art deco, romantic styles, full red or basic contrasting colors (red/green, purple/orange etc)

```html
<!DOCTYPE html>
<html lang="en">
<head>
<meta charset="utf-8">
<title>nelo architecture – folder spread</title>
<link rel="stylesheet" href="https://fonts.googleapis.com/css2?family=Comfortaa:wght@400;500&family=EB+Garamond:ital,wght@0,600;1,600&display=swap">
<style>
  :root {
    --page-bg: #ffffff;
    --leaf-green: #b3ba3c;
    --leaf-deep: #8a9228;
    --leaf-shadow: #7f8722;
    --cream: #e8edc9;
    --cream-soft: rgba(232, 237, 201, 0.85);
    --olive-text: #6f7420;
    --ghost: rgba(255, 255, 255, 0.09);
  }
  * { box-sizing: border-box; margin: 0; padding: 0; }
  html, body {
    width: 1200px; height: 719px; overflow: hidden;
    background: var(--page-bg);
  }
  .canvas { position: relative; width: 1200px; height: 719px; }

  .spread {
    position: absolute; left: 50px; top: 80px;
    width: 1100px; height: 560px;
    display: flex; overflow: hidden;
  }
  .panel { position: relative; width: 550px; height: 560px; overflow: hidden; }
  .panel--back {
    background: linear-gradient(100deg, var(--leaf-green) 0%, var(--leaf-green) 42%, var(--leaf-deep) 100%);
  }
  .panel--front {
    background: linear-gradient(80deg, var(--leaf-deep) 0%, var(--leaf-green) 45%, var(--leaf-green) 100%);
  }

  .ghost-word {
    position: absolute; top: 120px;
    font-family: "Comfortaa", sans-serif; font-weight: 500;
    font-size: 380px; line-height: 1; letter-spacing: -6px;
    color: var(--ghost); white-space: nowrap;
  }
  .panel--back .ghost-word { left: 250px; }
  .panel--front .ghost-word { left: -300px; }

  .back-tag {
    position: absolute; left: 26px; top: 40px;
    font-family: "Comfortaa", sans-serif; font-size: 22px;
    color: rgba(255, 255, 255, 0.12); letter-spacing: 1px;
  }

  .contact-block {
    position: absolute; left: 270px; bottom: 34px; width: 250px;
    color: var(--cream-soft);
    font-family: "EB Garamond", serif; font-weight: 600; font-size: 8px; line-height: 1.35;
  }
  .contact-block .rule { height: 1px; background: var(--cream-soft); margin-bottom: 6px; }
  .contact-block .rule--short { margin: 6px 0 6px; }
  .contact-name {
    font-family: "Comfortaa", sans-serif; font-weight: 400; font-size: 15px;
    color: var(--cream); text-align: right; margin: 0 0 4px;
  }
  .contact-row { display: flex; justify-content: space-between; align-items: flex-start; }
  .contact-item { display: flex; gap: 5px; align-items: flex-start; }
  .contact-item svg { flex: none; margin-top: 1px; }
  .social-square { width: 8px; height: 8px; background: var(--cream-soft); flex: none; margin-top: 1px; }
  .align-right { text-align: right; }

  .brand {
    position: absolute; right: 38px; top: 160px; text-align: right;
  }
  .brand-mark {
    display: inline-block; width: 54px; height: 54px; border-radius: 50%;
    background: var(--cream); margin-bottom: 18px;
  }
  .brand-name {
    font-family: "Comfortaa", sans-serif; font-weight: 500; font-size: 26px;
    color: var(--cream); letter-spacing: 0.5px;
  }
  .brand-name-gr {
    font-family: "EB Garamond", serif; font-weight: 600; font-size: 20px;
    color: var(--olive-text); margin-top: 2px;
  }
</style>
</head>
<body>
<main class="canvas">
  <section class="spread">
    <article class="panel panel--back">
      <span class="ghost-word" aria-hidden="true">nelo</span>
      <p class="back-tag">nelo architecture</p>

      <footer class="contact-block">
        <div class="rule"></div>
        <p class="contact-name">nelo architecture</p>
        <div class="contact-row">
          <div class="contact-item">
            <svg width="6" height="9" viewBox="0 0 6 9" aria-hidden="true"><rect x="0.5" y="0.5" width="5" height="8" rx="1" fill="none" stroke="#e8edc9"/></svg>
            <span>P: (555) 014-2290<br>F: (555) 014-2291</span>
          </div>
          <div class="contact-item">
            <svg width="10" height="7" viewBox="0 0 10 7" aria-hidden="true"><rect x="0.5" y="0.5" width="9" height="6" fill="none" stroke="#e8edc9"/><path d="M0.5 0.5 5 4 9.5 0.5" fill="none" stroke="#e8edc9"/></svg>
            <span class="align-right">info@neloarchitecture.com<br>neloarchitecture.com</span>
          </div>
          <div class="contact-item">
            <span class="social-square"></span>
            <span>@neloarchitecture</span>
          </div>
        </div>
        <div class="rule rule--short"></div>
        <div class="contact-row" style="justify-content:flex-end">
          <div class="contact-item">
            <svg width="7" height="10" viewBox="0 0 7 10" aria-hidden="true"><path d="M3.5 10C1.5 6.8 0 5.2 0 3.5a3.5 3.5 0 0 1 7 0c0 1.7-1.5 3.3-3.5 6.5z" fill="#e8edc9"/><circle cx="3.5" cy="3.5" r="1.3" fill="#9aa22e"/></svg>
            <span class="align-right">1420 Meadow Ridge Ave. Ste. 8<br>Fort Alder, CO 80777</span>
          </div>
        </div>
      </footer>
    </article>

    <article class="panel panel--front">
      <span class="ghost-word" aria-hidden="true">nelo</span>
      <header class="brand">
        <span class="brand-mark" aria-hidden="true"></span>
        <h1 class="brand-name">nelo architecture</h1>
        <p class="brand-name-gr" lang="el">nelo αρχιτεκτονική</p>
      </header>
    </article>
  </section>
</main>
</body>
</html>
```